Brightmere Business Card Redesign & Logo Update

We need to update our business cards to something more modern and fresh. Brightmere can provide the current color schemes and old design examples, but welcome creativity in helping us with this redesign. PLEASE NOTE that we no longer utilize the "tree" and/or "leaf" imagery in our branding. If able would apprecaite an update on the quality of our "words only" logo in Ai. / PNG formats too.

Target Market(s)

Investors, landowners, corporate partners, contractors

Industry/Entity Type

Environmental Restoration & Conservation

Contact Information for Business Card

Logo, persons name, title, mailing address, phone and email, website url

Font styles to use
Other font styles liked:
• Merriweather

Requirements
Nice to have
• Logo, persons name, title, mailing address, phone and email, website url, but open to ideams
Should not have
• No all back backgrounds

```html
<!DOCTYPE html>
<html lang="en">
<head>
<meta charset="utf-8">
<title>Brightmere Business Card</title>
<link href="https://fonts.googleapis.com/css2?family=Montserrat:wght@400;500;700;800&display=swap" rel="stylesheet">
<style>
  :root {
    --orange: #ee7f23;
    --green: #137a3a;
    --ink: #1f1f1f;
    --paper: #ffffff;
    --backdrop: #2b2b2b;
  }
  * { margin: 0; padding: 0; box-sizing: border-box; }
  html, body {
    width: 1200px; height: 900px; overflow: hidden;
    background: var(--backdrop);
    font-family: "Montserrat", sans-serif;
  }
  .canvas {
    width: 1200px; height: 900px;
    display: flex; flex-direction: column; align-items: center; justify-content: center;
    gap: 44px;
  }
  .card {
    width: 700px; height: 400px;
    border-radius: 26px;
    position: relative;
    overflow: hidden;
  }
  .card--front {
    background: var(--paper);
    display: flex; align-items: center;
    padding: 0 48px;
  }
  .brand {
    flex: 0 0 300px;
    display: flex; align-items: center; gap: 12px;
  }
  .brand__mark {
    width: 14px; height: 14px; background: var(--green); flex: none;
  }
  .brand__name {
    font-weight: 800; font-size: 36px; letter-spacing: 0.5px;
    color: var(--green); text-transform: uppercase;
    white-space: nowrap;
  }
  .divider {
    width: 1px; height: 210px; background: var(--green);
    margin: 0 30px 0 18px;
  }
  .contact { color: var(--ink); white-space: nowrap; }
  .contact__name {
    font-weight: 800; font-size: 22px; letter-spacing: 1.5px; text-transform: uppercase;
  }
  .contact__first { color: var(--green); }
  .contact__last { color: var(--orange); }
  .contact__title { font-size: 15px; margin: 4px 0 16px; }
  .contact__address { font-size: 15px; line-height: 1.45; margin-bottom: 12px; }
  .contact__line {
    display: flex; align-items: center; gap: 8px;
    font-size: 15px; line-height: 1.6;
  }
  .contact__line svg { width: 13px; height: 13px; flex: none; }
  .card--back {
    background: var(--orange);
    display: flex; align-items: center; justify-content: center;
  }
  .card--back .brand__name {
    color: var(--paper); font-size: 72px; letter-spacing: 2px;
  }
</style>
</head>
<body>
<main class="canvas">
  <section class="card card--front" aria-label="Business card front">
    <div class="brand">
      <span class="brand__mark"></span>
      <span class="brand__name">Brightmere</span>
    </div>
    <div class="divider"></div>
    <div class="contact">
      <p class="contact__name"><span class="contact__first">Mara</span> <span class="contact__last">Ellison</span></p>
      <p class="contact__title">CEO/Founder</p>
      <p class="contact__address">48 Harbor Lane<br>Lakeview, ON 40291</p>
      <p class="contact__line">
        <svg viewBox="0 0 16 16"><path fill="#ee7f23" d="M3.6 1.5l2.3 2.6-1.3 1.8c.9 2 2.5 3.6 4.5 4.5l1.8-1.3 2.6 2.3-1.4 2.1C6.8 14.3 1.7 9.2 1.5 3z"/></svg>
        (555) 018 2247
      </p>
      <p class="contact__line">
        <svg viewBox="0 0 16 16"><rect x="1" y="3" width="14" height="10" fill="#ee7f23"/><path d="M1 3l7 6 7-6" fill="none" stroke="#fff" stroke-width="1.3"/></svg>
        mara@brightmere.com
      </p>
      <p class="contact__line">
        <svg viewBox="0 0 16 16"><circle cx="8" cy="8" r="7" fill="#ee7f23"/><path d="M1 8h14M8 1c-3 3.5-3 10.5 0 14M8 1c3 3.5 3 10.5 0 14" fill="none" stroke="#fff" stroke-width="1"/></svg>
        www.brightmere.com
      </p>
    </div>
  </section>
  <section class="card card--back" aria-label="Business card back">
    <span class="brand__name">Brightmere</span>
  </section>
</main>
</body>
</html>
```